Wendelmarsh general contractors post card for mailing

Ideas: bathrooms, basements, kitchens, drywall, painting, landscaping, plumbing, electric, appliance, flooring, trim, sheds, decks, fences, home building, commercial construction, property management, lawn care/maintenance Just to list a few!!!

If we can't do it... it can't be done right.

turning dreams and aspirations into affordable reality.

Did your last contractor fail to meet your expectations? Let us provide affordable corrections.

Your single point of success for all your repair, replace, renovation, and building needs.

Trust us with all your projects large and small.

Target Market(s)

Home owners commercial property owners

Industry/Entity Type

Construction Company

Requirements
Must have
• phone number in red
Nice to have
• I would like to see greyscale background of commercial and suburban housing as a faded canvas backdrop.

```html
<!DOCTYPE html>
<html lang="en">
<head>
<meta charset="utf-8">
<title>Wendelmarsh General Contractors – Postcard</title>
<link href="https://fonts.googleapis.com/css2?family=Montserrat:wght@600;700;800&family=Open+Sans:wght@400;600&display=swap" rel="stylesheet">
<style>
  :root{
    --navy:#1d2a5c;
    --blue:#2f6fd0;
    --blue-light:#4d93e8;
    --white:#ffffff;
    --ink:#1d2a5c;
    --red:#d8232a;
    --paper:#eef0f4;
    --stamp:#d9dce2;
    --photo-sky:#9fb6cf;
    --photo-house:#b9a894;
    --photo-lawn:#5f7a4a;
  }
  *{box-sizing:border-box;margin:0;padding:0}
  html,body{width:900px;height:1200px;overflow:hidden}
  body{background:var(--paper);position:relative;font-family:"Open Sans",Arial,sans-serif;color:var(--ink)}
  .postcard{position:absolute;left:50px;width:800px;height:540px;background:var(--white);overflow:hidden;box-shadow:0 4px 14px rgba(0,0,0,.18)}
  .postcard--front{top:40px}
  .postcard--back{top:620px}
  .abs{position:absolute}

  /* front */
  .hero-photo{left:250px;top:0;width:550px;height:370px;
    background:linear-gradient(180deg,var(--photo-sky) 0%,#c7d3e0 40%,var(--photo-house) 62%,var(--photo-lawn) 100%);
    clip-path:polygon(60px 0,100% 0,100% 100%,0 100%)}
  .front-question{left:0;top:0;width:300px;height:78px;padding:16px 20px 0;font-family:"Montserrat",sans-serif;font-weight:800;font-size:17px;line-height:1.25;color:var(--navy)}
  .front-correction{left:0;top:78px;width:320px;height:140px;background:var(--blue);clip-path:polygon(0 0,100% 0,88% 100%,0 100%);padding:14px 20px;color:var(--white)}
  .front-correction h2{font-family:"Montserrat",sans-serif;font-weight:800;font-size:22px;line-height:1.15;margin-bottom:8px}
  .front-correction p{font-size:10.5px;line-height:1.4;width:230px}
  .front-promise{left:0;top:218px;width:300px;height:78px;background:var(--navy);clip-path:polygon(0 0,100% 0,92% 100%,0 100%);padding:14px 20px;color:var(--white);font-family:"Montserrat",sans-serif}
  .front-promise .big{font-weight:800;font-size:21px;line-height:1.1}
  .front-promise .small{font-weight:700;font-size:13px;margin-top:4px}
  .front-web{left:0;top:296px;width:280px;height:46px;padding:12px 20px 0;font-family:"Montserrat",sans-serif;font-weight:800;font-size:16px;white-space:nowrap;color:var(--navy);border-bottom:4px solid var(--blue)}
  .brand{display:flex;align-items:center;gap:10px}
  .brand-mark{width:26px;height:26px;background:var(--navy)}
  .brand-name{font-family:"Montserrat",sans-serif;font-weight:700;font-size:22px;letter-spacing:1px;color:var(--navy)}
  .phone{font-family:"Montserrat",sans-serif;font-weight:700;font-size:13px;color:var(--red);margin-top:4px;padding-left:36px}
  .front-brand{left:20px;top:400px}
  .front-band{left:280px;top:380px;width:520px;height:160px;background:linear-gradient(90deg,var(--navy),var(--blue) 45%,var(--blue-light));clip-path:polygon(20px 0,100% 0,100% 100%,0 100%)}
  .tagline{left:300px;top:470px;width:490px;text-align:center;color:var(--white);font-family:"Montserrat",sans-serif}
  .tagline .line1{font-weight:700;font-size:19px}
  .tagline .line2{font-weight:800;font-size:25px}
  .circle-photo{width:122px;height:122px;border-radius:50%;border:5px solid var(--white);top:312px;
    background:linear-gradient(160deg,var(--photo-sky),var(--photo-house) 60%,var(--photo-lawn))}

  /* back */
  .back-headline{left:30px;top:30px;width:470px;font-family:"Montserrat",sans-serif;font-weight:700;font-size:21px;line-height:1.3;color:var(--navy)}
  .stamp{right:30px;top:26px;width:100px;height:110px;background:var(--stamp)}
  .back-band{left:0;top:160px;width:800px;height:190px;background:linear-gradient(90deg,var(--blue),var(--blue-light));clip-path:polygon(0 20%,72% 0,100% 0,100% 40%,55% 100%,0 100%)}
  .square-photo{top:168px;width:110px;height:110px;border:5px solid var(--white);
    background:linear-gradient(170deg,var(--photo-sky),var(--photo-house) 60%,var(--photo-lawn))}
  .services{left:0;top:300px;width:470px;height:210px;background:var(--navy);clip-path:polygon(0 0,100% 0,88% 100%,0 100%);padding:22px 30px;color:var(--white)}
  .services h3{font-family:"Montserrat",sans-serif;font-weight:800;font-size:19px;margin-bottom:10px}
  .services ul{list-style:none}
  .services li{display:flex;align-items:center;gap:10px;font-size:14px;line-height:1.75}
  .services li::before{content:"";width:9px;height:9px;border-radius:50%;background:var(--white);flex:none}
  .back-brand{right:40px;top:400px}
  .back-strip{left:0;top:512px;width:800px;height:28px;background:var(--navy)}
</style>
</head>
<body>

<section class="postcard postcard--front">
  <div class="abs hero-photo" role="img" aria-label="Photo of a large two-storey suburban house with a lawn"></div>
  <div class="abs front-question">Did your last contractor fail to meet your expectations?</div>
  <div class="abs front-correction">
    <h2>Let us provide you affordable corrections</h2>
    <p>We fix what others left undone. Quality repairs, honest pricing and skilled crews for every home and commercial project.</p>
  </div>
  <div class="abs front-promise">
    <div class="big">IF WE CAN'T DO IT</div>
    <div class="small">IT CAN'T BE DONE RIGHT</div>
  </div>
  <div class="abs front-web">www.wendelmarsh.com</div>
  <div class="abs front-band"></div>
  <div class="abs circle-photo" style="left:330px" role="img" aria-label="Photo of a renovated house exterior"></div>
  <div class="abs circle-photo" style="left:480px" role="img" aria-label="Photo of a finished interior room"></div>
  <div class="abs circle-photo" style="left:630px" role="img" aria-label="Photo of a newly built home"></div>
  <div class="abs tagline">
    <div class="line1">TURNING DREAMS &amp; ASPIRATIONS</div>
    <div class="line2">INTO AFFORDABLE REALITY</div>
  </div>
  <div class="abs front-brand">
    <div class="brand"><span class="brand-mark"></span><span class="brand-name">WENDELMARSH</span></div>
    <div class="phone">1-800-555-0142</div>
  </div>
</section>

<section class="postcard postcard--back">
  <div class="abs back-headline">Your single point of success for all your repair, replace, renovation, and building needs.</div>
  <div class="abs stamp"></div>
  <div class="abs back-band"></div>
  <div class="abs square-photo" style="left:40px" role="img" aria-label="Photo of a brick family home"></div>
  <div class="abs square-photo" style="left:170px" role="img" aria-label="Photo of a house under renovation"></div>
  <div class="abs square-photo" style="left:300px" role="img" aria-label="Photo of a suburban house with porch"></div>
  <div class="abs services">
    <h3>OUR SERVICES</h3>
    <ul>
      <li>Lorem ipsum dolor sit amet</li>
      <li>Lorem ipsum dolor sit</li>
      <li>Lorem ipsum dolor sit amet</li>
      <li>Lorem ipsum dolor sit amet</li>
      <li>Lorem ipsum dolor sit amet</li>
    </ul>
  </div>
  <div class="abs back-brand">
    <div class="brand"><span class="brand-mark"></span><span class="brand-name">WENDELMARSH</span></div>
    <div class="phone">1-800-555-0142</div>
  </div>
  <div class="abs back-strip"></div>
</section>

</body>
</html>
```